Thank you cards for online orders

We have a logo that is attached and I'd for it to be used to make a thank you card that will give our clients some info on product care as well as refund/exchange policy. so maybe a small package that includes a thank you card, and policy details
Updates

Sick

Target Market(s)

Females for 20-70

```html
<!DOCTYPE html>
<html lang="en">
<head>
<meta charset="utf-8">
<title>Corvella Thank You Card</title>
<link rel="stylesheet" href="https://fonts.googleapis.com/css2?family=Josefin+Sans:wght@400;600&family=Cinzel:wght@400&family=Parisienne&display=swap">
<style>
  :root {
    --backdrop: #bcbdc0;
    --card: #ffffff;
    --brand-green: #9dbf2f;
    --text-grey: #8f958f;
    --script-grey: #939b93;
    --wave: #eef0f3;
  }
  * { margin: 0; padding: 0; box-sizing: border-box; }
  html, body {
    width: 1200px;
    height: 997px;
    overflow: hidden;
    background: var(--backdrop);
  }
  .canvas {
    position: relative;
    width: 1200px;
    height: 997px;
  }
  .card {
    position: absolute;
    top: 47px;
    height: 901px;
    background: var(--card);
    overflow: hidden;
  }
  .card--front { left: 50px; width: 505px; }
  .card--back { left: 631px; width: 509px; }
  .card__waves {
    position: absolute;
    inset: 0;
    width: 100%;
    height: 100%;
  }
  .brand {
    position: absolute;
    left: 0;
    right: 0;
    text-align: center;
  }
  .brand__name {
    display: block;
    font-family: "Josefin Sans", sans-serif;
    font-weight: 400;
    font-size: 56px;
    letter-spacing: 3px;
    color: var(--brand-green);
    line-height: 1;
  }
  .brand__est {
    display: block;
    margin-top: 16px;
    font-family: "Cinzel", serif;
    font-size: 16px;
    letter-spacing: 3px;
    color: var(--text-grey);
    line-height: 1;
  }
  .card--front .brand { top: 78px; }
  .card--back .brand { top: 764px; }
  .thanks {
    position: absolute;
    left: 0;
    right: 0;
    top: 255px;
    font-family: "Parisienne", cursive;
    color: var(--script-grey);
    text-align: center;
    line-height: 1;
  }
  .thanks__line {
    display: block;
    font-size: 132px;
  }
  .thanks__line--second {
    margin-top: -10px;
    font-size: 120px;
    padding-left: 20px;
  }
  .mandala {
    position: absolute;
    left: 10px;
    top: 600px;
    width: 490px;
    height: 301px;
  }
  .policy {
    position: absolute;
    left: 46px;
    right: 46px;
    top: 74px;
    font-family: "Josefin Sans", sans-serif;
    color: var(--text-grey);
    font-size: 25.5px;
    line-height: 36px;
    text-align: justify;
  }
  .policy__title {
    font-weight: 600;
    font-size: 25px;
    letter-spacing: 1px;
    text-align: center;
  }
  .policy__para { text-align-last: center; }
</style>
</head>
<body>
<div class="canvas">

  <section class="card card--front">
    <svg class="card__waves" viewBox="0 0 505 901" preserveAspectRatio="none" aria-hidden="true">
      <path d="M0 370 C120 300 260 330 505 470 L505 560 C300 420 150 410 0 470 Z" fill="var(--wave)"/>
    </svg>
    <div class="brand">
      <span class="brand__name">CORVELLA</span>
      <span class="brand__est">EST. 2006</span>
    </div>
    <h1 class="thanks">
      <span class="thanks__line">Thank</span>
      <span class="thanks__line thanks__line--second">you</span>
    </h1>
    <svg class="mandala" viewBox="0 0 490 301" role="img" aria-label="Green mandala ornament rising from the bottom edge">
      <defs>
        <linearGradient id="mandalaTone" x1="0" y1="0" x2="1" y2="1">
          <stop offset="0" stop-color="#5e8a1f"/>
          <stop offset="1" stop-color="#b5d334"/>
        </linearGradient>
      </defs>
      <path d="M0 301 A245 290 0 0 1 490 301 Z" fill="url(#mandalaTone)" opacity="0.85"/>
    </svg>
  </section>

  <section class="card card--back">
    <svg class="card__waves" viewBox="0 0 509 901" preserveAspectRatio="none" aria-hidden="true">
      <path d="M0 150 C150 120 330 180 509 90 L509 150 C340 250 150 190 0 230 Z" fill="var(--wave)"/>
      <path d="M0 560 C180 600 360 560 509 480 L509 560 C360 640 180 670 0 650 Z" fill="var(--wave)"/>
    </svg>
    <div class="policy">
      <p class="policy__title">REFUNDS</p>
      <p class="policy__para">Once we receive the item(s) they will be inspected, and an email will be sent to notify you of the approval or rejection of your refund.</p>
      <p class="policy__para">If you are approved, then your refund will be processed minus a re-stocking fee of 10% and a credit will automatically be issued in your original method of payment, within 5-10 business days.</p>
      <p class="policy__para">Why a re-stocking fee? Corvella charges a 10% restocking fee to help cover any processing fees, handling, and other costs associa&shy;ted with processing returns.</p>
    </div>
    <div class="brand">
      <span class="brand__name">CORVELLA</span>
      <span class="brand__est">EST. 2006</span>
    </div>
  </section>

</div>
</body>
</html>
```